Redesign of iOS App Lumo Tutor

Redesign of existing App Lumo Tutor, an app that helps learning Japanese Kanjis, Hiragana, Katakana.

The functionallity should remain the same as today: the app is free, you may download it at the app store. But: I like the design of my other apps better ;)

Target Market(s)

Students learning Japanese

Industry/Entity Type

Teacher

Font styles to use
Sans Serif

Requirements
Must have
• Lumo Tutor has 7 main screens, all screens has to be designed for iPhone and iPad: Main, Settings, Reading Tests, Writing Tests, Game, Paper Mode, Search
Nice to have
• I like the logo as it is today

```html
<!DOCTYPE html>
<html lang="en">
<head>
<meta charset="utf-8">
<title>Lumo Tutor – Search</title>
<link href="https://fonts.googleapis.com/css2?family=Nunito:wght@400;700&family=Noto+Sans+JP:wght@400&display=swap" rel="stylesheet">
<style>
  :root{
    --ink:#222;
    --ink-soft:#444;
    --muted:#9d9d9d;
    --placeholder:#cfcfcf;
    --rule:#dcdcdc;
    --rule-strong:#9a9a9a;
    --bar:#e6e7e8;
    --star:#c9c9c9;
    --paper:#ffffff;
    --button:#f4f4f4;
    --mark-grey:#9b9b9b;
    --mark-red:#f25c4b;
    --mark-blue:#5799d2;
    --mark-teal:#20bca8;
    --star-dark:#3a3a3a;
  }
  *{margin:0;padding:0;box-sizing:border-box}
  html,body{width:675px;height:1200px;overflow:hidden;background:var(--paper)}
  body{font-family:"Nunito",sans-serif;color:var(--ink);position:relative}
  .screen{position:relative;width:675px;height:1200px;overflow:hidden}

  .status-bar{position:absolute;top:0;left:0;width:675px;height:36px;font-size:17px;color:#111}
  .status-bar .signal{position:absolute;left:12px;top:13px;display:flex;gap:3px}
  .status-bar .signal i{width:9px;height:9px;border-radius:50%;background:#222;display:block}
  .status-bar .wifi{position:absolute;left:82px;top:8px}
  .status-bar .time{position:absolute;left:0;width:675px;text-align:center;top:6px}
  .status-bar .battery-label{position:absolute;right:72px;top:6px}
  .status-bar .battery{position:absolute;right:16px;top:10px}

  .top-band{position:absolute;left:34px;top:36px;width:606px;height:43px;background:var(--bar)}
  .search-field{position:absolute;left:32px;top:93px;font-size:23px;color:var(--placeholder);letter-spacing:.5px}
  .help-button{position:absolute;left:526px;top:94px;width:114px;height:31px;border-radius:16px;background:var(--muted);color:#fff;font-size:19px;text-align:center;line-height:31px;border:1px solid #8c8c8c}
  .search-rule{position:absolute;left:34px;top:149px;width:609px;height:2px;background:var(--rule-strong)}

  .kana-list{position:absolute;left:34px;top:151px;width:609px;list-style:none}
  .kana-row{position:relative;height:118px;border-bottom:2px solid var(--rule)}
  .kana-glyph{position:absolute;left:6px;top:10px;font-family:"Noto Sans JP",sans-serif;font-size:70px;line-height:90px;color:#111}
  .romaji{position:absolute;left:116px;top:30px;font-size:17px;color:var(--ink-soft)}
  .progress{position:absolute;left:116px;top:66px;display:flex;gap:4px}
  .progress i{width:13px;height:13px;border-radius:50%;background:var(--placeholder);display:block}
  .script-name{position:absolute;left:255px;top:44px;font-size:20px;font-weight:700;color:var(--ink-soft);letter-spacing:.6px}
  .fav{position:absolute;left:532px;top:30px}

  .filter-panel{position:absolute;left:279px;top:727px;width:361px;height:438px;background:var(--paper);border:1.5px solid var(--rule)}
  .practice-button{position:absolute;left:59px;top:27px;width:241px;height:33px;border:1.5px solid #c8c8c8;border-radius:17px;text-align:center;line-height:30px;font-size:20px;color:var(--ink-soft)}
  .panel-heading{position:absolute;left:0;width:361px;display:flex;align-items:center;font-size:26px;color:var(--ink-soft)}
  .panel-heading::before,.panel-heading::after{content:"";flex:1;height:1.5px;background:var(--rule)}
  .panel-heading span{padding:0 12px}
  .heading-tests{top:91px}
  .heading-kanjis{top:229px}
  .heading-kanjis::after{margin-right:-4px}
  .test-marks{position:absolute;top:218px;left:32px;display:flex;gap:24px}
  .test-marks i{width:57px;height:57px;border-radius:50%;display:block;border:1px solid rgba(0,0,0,.18)}
  .test-marks{top:149px}
  .mark-grey{background:var(--mark-grey)}
  .mark-red{background:var(--mark-red)}
  .mark-blue{background:var(--mark-blue)}
  .mark-teal{background:var(--mark-teal)}
  .kanji-marks{position:absolute;top:278px;left:111px;display:flex;gap:22px}
  .panel-footer{position:absolute;left:0;bottom:0;width:100%;height:70px;border-top:1.5px solid var(--rule)}
  .result-count{position:absolute;left:24px;top:22px;font-size:19px;color:var(--ink-soft)}
  .expand{position:absolute;right:30px;top:22px}

  .home-button{position:absolute;left:34px;top:1094px;width:139px;height:54px;background:var(--button);border:1.5px solid #c4c4c4;border-radius:4px;font-size:20px;font-weight:700;color:var(--ink-soft);text-align:center;line-height:51px;letter-spacing:.5px}
</style>
</head>
<body>
<div class="screen">
  <div class="status-bar">
    <div class="signal"><i></i><i></i><i></i><i></i><i></i></div>
    <svg class="wifi" width="22" height="17" viewBox="0 0 22 17"><path d="M11 16 L7 11.5 A6 6 0 0 1 15 11.5 Z M2.5 7 A12 12 0 0 1 19.5 7 L17.5 9.2 A9 9 0 0 0 4.5 9.2 Z M0 4.2 A16 16 0 0 1 22 4.2 L20.6 5.7 A14 14 0 0 0 1.4 5.7 Z" fill="#222"/></svg>
    <div class="time">9:41 AM</div>
    <div class="battery-label">100%</div>
    <svg class="battery" width="52" height="18" viewBox="0 0 52 18"><rect x="1" y="1" width="45" height="16" rx="3" fill="none" stroke="#333" stroke-width="1.5"/><rect x="3" y="3" width="41" height="12" rx="1.5" fill="#333"/><rect x="47.5" y="6" width="3" height="6" rx="1" fill="#333"/></svg>
  </div>

  <div class="top-band"></div>
  <div class="search-field">Search</div>
  <div class="help-button">help</div>
  <div class="search-rule"></div>

  <ul class="kana-list">
    <li class="kana-row"><span class="kana-glyph">あ</span><span class="romaji">a</span><span class="progress"><i></i><i></i><i></i></span><span class="script-name">Hiragana</span><svg class="fav" width="62" height="60" viewBox="0 0 100 100"><polygon points="50,5 61,38 96,38 68,59 79,93 50,72 21,93 32,59 4,38 39,38" fill="none" stroke="var(--star)" stroke-width="6" stroke-linejoin="miter"/></svg></li>
    <li class="kana-row"><span class="kana-glyph">い</span><span class="romaji">i</span><span class="progress"><i></i><i></i><i></i></span><span class="script-name">Hiragana</span><svg class="fav" width="62" height="60" viewBox="0 0 100 100"><polygon points="50,5 61,38 96,38 68,59 79,93 50,72 21,93 32,59 4,38 39,38" fill="none" stroke="var(--star)" stroke-width="6"/></svg></li>
    <li class="kana-row"><span class="kana-glyph">う</span><span class="romaji">u</span><span class="progress"><i></i><i></i><i></i></span><span class="script-name">Hiragana</span><svg class="fav" width="62" height="60" viewBox="0 0 100 100"><polygon points="50,5 61,38 96,38 68,59 79,93 50,72 21,93 32,59 4,38 39,38" fill="none" stroke="var(--star)" stroke-width="6"/></svg></li>
    <li class="kana-row"><span class="kana-glyph">え</span><span class="romaji">e</span><span class="progress"><i></i><i></i><i></i></span><span class="script-name">Hiragana</span><svg class="fav" width="62" height="60" viewBox="0 0 100 100"><polygon points="50,5 61,38 96,38 68,59 79,93 50,72 21,93 32,59 4,38 39,38" fill="none" stroke="var(--star)" stroke-width="6"/></svg></li>
    <li class="kana-row"><span class="kana-glyph">お</span><span class="romaji">o</span><span class="progress"><i></i><i></i><i></i></span><span class="script-name">Hiragana</span><svg class="fav" width="62" height="60" viewBox="0 0 100 100"><polygon points="50,5 61,38 96,38 68,59 79,93 50,72 21,93 32,59 4,38 39,38" fill="none" stroke="var(--star)" stroke-width="6"/></svg></li>
    <li class="kana-row"><span class="kana-glyph">か</span><span class="romaji">ka</span><span class="progress"><i></i><i></i><i></i></span></li>
    <li class="kana-row"><span class="kana-glyph">が</span><span class="romaji">ga</span><span class="progress"><i></i><i></i><i></i></span></li>
  </ul>

  <div class="filter-panel">
    <div class="practice-button">Practice Writing</div>
    <div class="panel-heading heading-tests"><span>Mark 30848 Tests</span></div>
    <div class="test-marks"><i class="mark-grey"></i><i class="mark-red"></i><i class="mark-blue"></i><i class="mark-teal"></i></div>
    <div class="panel-heading heading-kanjis"><span>Mark 2136 Kanjis</span></div>
    <div class="kanji-marks">
      <svg width="60" height="58" viewBox="0 0 100 100"><polygon points="50,5 61,38 96,38 68,59 79,93 50,72 21,93 32,59 4,38 39,38" fill="none" stroke="var(--star-dark)" stroke-width="6"/></svg>
      <svg width="60" height="58" viewBox="0 0 100 100"><polygon points="50,5 61,38 96,38 68,59 79,93 50,72 21,93 32,59 4,38 39,38" fill="var(--star-dark)"/></svg>
    </div>
    <div class="panel-footer">
      <span class="result-count">2278 entries found</span>
      <svg class="expand" width="32" height="28" viewBox="0 0 32 28"><polygon points="1,1 31,1 16,27" fill="none" stroke="#d4d4d4" stroke-width="1.5"/></svg>
    </div>
  </div>

  <div class="home-button">Home</div>
</div>
</body>
</html>
```